Boom Way Hoist Service Business Cards

I need a business card for "Boom Way Hoist and Haulage"

Boomway2023@hoistmail.net

Hoist Works LLC, Boom Way Hoist and Haulage LLC

555.014.7260 | www.BOOMWAYHOISTS.example

Central Indiana & Northeast Ohio

(IN) 14820 Maple Lane Noblesville, IN 46000

(OH) 2450 Pell Street Akron, Ohio 44300

Colors
0094D4
00A9DD
6FCCEA
C7EBF8
E9F6FB
59FF00
82FF00
B8FF75
E3FFCB
F4FFEA
EE7325
F08F49
F5BC92
FAE3D3
FDF4ED
EB3D1F
EC4F4E
F09395
F8D3D4
FCEDEE
E54698
E96AAD
F1A4CE
F9D9EA
FCEFF6
A7469A
B969AE
D3A5CF
EDDBEB
F8F0F9

```html
<!DOCTYPE html>
<html lang="en">
<head>
<meta charset="utf-8">
<title>Boom Way Hoist Service Business Cards</title>
<link href="https://fonts.googleapis.com/css2?family=Montserrat:wght@400;500;600;800&display=swap" rel="stylesheet">
<style>
  :root {
    --bg: #3a3a3a;
    --card-black: #141414;
    --white: #ffffff;
    --green: #2fc13e;
    --ink: #111111;
    --text-light: #f2f2f2;
  }
  * { box-sizing: border-box; margin: 0; padding: 0; }
  html, body { width: 1200px; height: 1200px; overflow: hidden; }
  body {
    background: var(--bg);
    font-family: "Montserrat", sans-serif;
    display: flex;
    flex-direction: column;
    align-items: center;
    justify-content: center;
    gap: 44px;
  }
  .card {
    width: 900px;
    height: 514px;
    border-radius: 34px;
    overflow: hidden;
    position: relative;
  }

  /* Front */
  .card--front { background: var(--card-black); }
  .front__top {
    position: absolute; inset: 0 0 auto 0; height: 232px;
    background: var(--white);
    display: flex; align-items: center; justify-content: center;
  }
  .brand { display: flex; align-items: center; gap: 16px; }
  .brand__mark { width: 26px; height: 26px; background: var(--green); }
  .brand__name {
    font-weight: 800; font-size: 44px; color: var(--ink);
    letter-spacing: 1px; text-transform: uppercase; line-height: 1.05;
  }
  .front__stripe {
    position: absolute; left: 0; right: 0; top: 232px; height: 14px;
    background: var(--green);
  }
  .front__body {
    position: absolute; left: 0; right: 0; top: 258px; bottom: 0;
    display: grid; grid-template-columns: 1fr 1fr; gap: 40px;
    padding: 30px 54px 0 70px;
  }
  .entities {
    color: var(--green); font-weight: 500; font-size: 19px;
    text-transform: uppercase; line-height: 1.25;
    padding-bottom: 12px; border-bottom: 2px solid var(--green);
  }
  .contact-list { list-style: none; margin-top: 14px; }
  .contact-list li {
    display: flex; align-items: center; gap: 14px;
    color: var(--text-light); font-size: 19px; line-height: 1.7;
  }
  .contact-list svg { width: 22px; height: 22px; flex: none; }
  .region {
    color: var(--green); font-weight: 600; font-size: 19px;
    padding-bottom: 10px; border-bottom: 2px solid var(--green);
    margin-bottom: 12px;
  }
  .address { color: var(--text-light); font-size: 17px; line-height: 1.6; }

  /* Back */
  .card--back {
    background: var(--card-black);
    display: flex; flex-direction: column; align-items: center; justify-content: center;
    gap: 26px;
  }
  .crane-art {
    width: 600px; height: 260px; border-radius: 10px;
    background: linear-gradient(135deg, #2a2a2a 0%, #1f5a27 60%, #2fc13e 100%);
  }
  .back-name {
    color: var(--white); font-weight: 800; font-size: 40px;
    text-transform: uppercase; letter-spacing: 1px;
    display: flex; align-items: center; gap: 16px;
  }
</style>
</head>
<body>

<section class="card card--front">
  <div class="front__top">
    <div class="brand">
      <span class="brand__mark"></span>
      <span class="brand__name">Boom Way<br>Hoist</span>
    </div>
  </div>
  <div class="front__stripe"></div>
  <div class="front__body">
    <div class="front__left">
      <p class="entities">Hoist Works LLC,<br>Boom Way Hoist and Haulage LLC</p>
      <ul class="contact-list">
        <li>
          <svg viewBox="0 0 24 24"><path fill="#2fc13e" d="M6.6 10.8a15.1 15.1 0 0 0 6.6 6.6l2.2-2.2c.3-.3.7-.4 1-.2 1.1.4 2.3.6 3.6.6.6 0 1 .4 1 1V20c0 .6-.4 1-1 1A17 17 0 0 1 3 4c0-.6.4-1 1-1h3.5c.6 0 1 .4 1 1 0 1.3.2 2.5.6 3.6.1.3 0 .7-.2 1z"/></svg>
          555.014.7260
        </li>
        <li>
          <svg viewBox="0 0 24 24"><rect x="2" y="5" width="20" height="14" fill="#2fc13e"/><path d="M2 5l10 8 10-8" fill="none" stroke="#141414" stroke-width="1.6"/></svg>
          Boomway2023@hoistmail.net
        </li>
        <li>
          <svg viewBox="0 0 24 24" fill="none" stroke="#2fc13e" stroke-width="1.8"><circle cx="12" cy="12" r="9.5"/><ellipse cx="12" cy="12" rx="4.5" ry="9.5"/><path d="M2.5 12h19M4 7h16M4 17h16"/></svg>
          www.BOOMWAYHOISTS.example
        </li>
      </ul>
    </div>
    <div class="front__right">
      <p class="region">Central Indiana &amp; Northeast Ohio</p>
      <p class="address">(IN) 14820 Maple Lane Noblesville, IN 46000</p>
      <p class="address">(OH) 2450 Pell Street Akron, Ohio 44300</p>
    </div>
  </div>
</section>

<section class="card card--back">
  <div class="crane-art" role="img" aria-label="Illustration of a mobile crane with extended boom and hook lines"></div>
  <div class="back-name">Boom Way Hoist and Haulage</div>
</section>

</body>
</html>
```